Buch-/eBook-Cover für professionelles Finanzbuch
Zielgruppe
Selbstständig in der Finanzaufklärung als Speaker und Verkäufer von Sachwerten
Aufgabenstellung
soll ein professionelles Finanzbuch sein von der Optik mit Foto von Technologiemetallen /Seltenen Erden

```html
<!DOCTYPE html>
<html lang="de">
<head>
<meta charset="utf-8">
<title>Generationenchance – Hightech-Metalle und kostbare Erze</title>
<link href="https://fonts.googleapis.com/css2?family=Barlow+Condensed:wght@500;600;700&family=Barlow:wght@500;600&display=swap" rel="stylesheet">
<style>
  :root {
    --cover-black: #0b0a09;
    --cover-deep: #050505;
    --gold-light: #f1dfb4;
    --gold-mid: #c9a45e;
    --gold-dark: #8a6a32;
    --band-light: #efe2c2;
    --band-dark: #b99a5d;
    --ink: #1a1610;
    --line-light: #e6e0d4;
  }
  * { margin: 0; padding: 0; box-sizing: border-box; }
  html, body { width: 930px; height: 1200px; overflow: hidden; background: #ffffff; }
  .cover {
    position: relative;
    width: 930px; height: 1200px;
    background: radial-gradient(ellipse at 50% 30%, #1c1a17 0%, var(--cover-black) 55%, var(--cover-deep) 100%);
    overflow: hidden;
  }
  .gold-text {
    background: linear-gradient(180deg, var(--gold-light) 0%, var(--gold-mid) 55%, var(--gold-dark) 100%);
    -webkit-background-clip: text; background-clip: text;
    color: transparent;
  }
  .ruled {
    display: flex; align-items: center; justify-content: center; gap: 18px;
    font-family: "Barlow", sans-serif; font-weight: 500;
    color: var(--line-light); text-transform: uppercase;
  }
  .ruled::before, .ruled::after {
    content: ""; height: 3px; background: var(--line-light);
  }
  .kicker { position: absolute; top: 62px; left: 0; right: 0; font-size: 36px; letter-spacing: 5px; }
  .kicker::before, .kicker::after { width: 42px; }
  .headline-top {
    position: absolute; top: 108px; left: 0; right: 0; text-align: center;
    font-family: "Barlow Condensed", sans-serif; font-weight: 700;
    font-size: 100px; line-height: 1; letter-spacing: 2px;
    transform: scaleY(1.12); transform-origin: top center;
  }
  .connector { position: absolute; top: 232px; left: 40px; right: 40px; }
  .connector .rule { position: absolute; top: 0; left: 0; right: 0; height: 3px; background: var(--gold-mid); }
  .connector .und {
    position: absolute; top: 14px; left: 0; right: 0;
    display: flex; align-items: center; justify-content: center; gap: 16px;
    font-family: "Barlow Condensed", sans-serif; font-weight: 700; font-size: 44px;
  }
  .connector .und::before, .connector .und::after { content: ""; width: 58px; height: 3px; background: var(--line-light); }
  .headline-main {
    position: absolute; top: 298px; left: 0; right: 0; text-align: center;
    font-family: "Barlow Condensed", sans-serif; font-weight: 700;
    font-size: 226px; line-height: 0.96; letter-spacing: 2px;
    transform: scaleY(1.08); transform-origin: top center;
  }
  .subline { position: absolute; top: 792px; left: 0; right: 0; font-size: 27px; letter-spacing: 1.5px; }
  .subline::before, .subline::after { width: 34px; height: 2px; }
  .visual {
    position: absolute; top: 840px; left: 0; right: 0; height: 225px;
    background:
      linear-gradient(90deg, rgba(11,10,9,0.9) 0%, rgba(11,10,9,0) 18%, rgba(11,10,9,0) 82%, rgba(11,10,9,0.85) 100%),
      linear-gradient(180deg, rgba(11,10,9,1) 0%, #3a2e1a 40%, #a8844a 70%, #2a2218 100%);
  }
  .author-band {
    position: absolute; left: 0; right: 0; bottom: 0; height: 135px;
    background: linear-gradient(180deg, var(--band-dark) 0%, var(--band-light) 28%, var(--band-light) 100%);
    display: flex; align-items: center; justify-content: center;
  }
  .author {
    font-family: "Barlow", sans-serif; font-weight: 600;
    font-size: 40px; letter-spacing: 4px; color: var(--ink); text-transform: uppercase;
    margin-top: 20px;
  }
</style>
</head>
<body>
  <main class="cover">
    <p class="ruled kicker">Generationenchance</p>
    <h1 class="headline-top gold-text">HIGHTECH-METALLE</h1>
    <div class="connector">
      <span class="rule"></span>
      <p class="und gold-text">UND</p>
    </div>
    <h2 class="headline-main gold-text">KOSTBARE<br>ERZE</h2>
    <p class="ruled subline">Vom Rohstoff zur Schlüsselressource</p>
    <div class="visual" role="img" aria-label="Foto glänzender Metallbarren in Gold- und Silbertönen, angeordnet wie ein Balkendiagramm"></div>
    <footer class="author-band">
      <p class="author">Lukas Brenner</p>
    </footer>
  </main>
</body>
</html>
```